Business Cards for Financial Service Consulting Business Ltd

Business Card Design for my risk management consultancy to the financial service industry
Responsible Lending, Fair Charges, Ethical Collections

Should be serious, professional, corporate

Target Market(s)

Fintech, Financial Services Industry

Industry/Entity Type

Financial Service

Contact Information for Business Card

Lewis Marsh
lew@slatewellconsulting.co.uk
07931520478
01632960417

Font styles to use
Serif

Colors

Designer to choose colors to be used in the design.

Requirements
Must have
• Name: Slatewell Consulting
• Logo, contact details
• The three pillars of my business Responsible Lending, Fair Charges, Ethical Collections
Nice to have
• Corporate Feel
Should not have
• jokes, pretty pictures, cartoons

```html
<!DOCTYPE html>
<html lang="en">
<head>
<meta charset="utf-8">
<title>Slatewell Consulting – Business Cards</title>
<link rel="stylesheet" href="https://fonts.googleapis.com/css2?family=Jost:wght@400;600;700&family=Montserrat:wght@500&display=swap">
<style>
  :root {
    --backdrop: #eeeeee;
    --card: #ffffff;
    --ink: #414143;
    --on-ink: #ffffff;
  }
  html, body {
    margin: 0;
    width: 1200px;
    height: 1096px;
    overflow: hidden;
    background: var(--backdrop);
  }
  .canvas { display: block; width: 1200px; height: 1096px; }
  .card-face { fill: var(--card); }
  .ink { fill: var(--ink); }
  .icon-line { fill: none; stroke: var(--ink); stroke-width: 1.6; stroke-linecap: round; stroke-linejoin: round; }
  .holder-name { font-family: "Jost", sans-serif; font-weight: 700; font-size: 28px; fill: var(--ink); }
  .holder-role { font-family: "Jost", sans-serif; font-weight: 400; font-size: 15.5px; fill: var(--ink); }
  .contact { font-family: "Jost", sans-serif; font-weight: 600; font-size: 16.5px; fill: var(--ink); }
  .band-text { font-family: "Jost", sans-serif; font-weight: 600; font-size: 16.5px; fill: var(--on-ink); }
  .pillar { font-family: "Montserrat", sans-serif; font-weight: 500; font-size: 17.5px; fill: var(--on-ink); }
  .brand-name { font-family: "Jost", sans-serif; font-weight: 700; fill: var(--ink); }
  .brand-primary { font-size: 40px; }
  .brand-secondary { font-size: 23px; }
</style>
</head>
<body>
<svg class="canvas" viewBox="0 0 1200 1096" xmlns="http://www.w3.org/2000/svg">

  <!-- Contact side -->
  <g class="card card-contact" transform="translate(491 167)">
    <rect class="card-face" width="550" height="356"/>

    <g class="contact-row holder">
      <circle class="icon-line" cx="34" cy="162" r="16.5"/>
      <circle class="icon-line" cx="34" cy="157" r="5.5"/>
      <path class="icon-line" d="M24 173 q10 -11 20 0"/>
      <text class="holder-name" x="61" y="164">Lewis Marsh</text>
      <text class="holder-role" x="61" y="180">Financial Counselor</text>
    </g>

    <g class="contact-row phones">
      <circle class="icon-line" cx="34" cy="220" r="16.5"/>
      <path class="icon-line" d="M27 212 l4 -2 l3 6 l-2.5 2 q2 5 6 7 l2 -2.5 l6 3 l-2 4 q-9 1 -16.5 -17.5z"/>
      <text class="contact" x="61" y="216">07931520478</text>
      <text class="contact" x="61" y="235">01632960417</text>
    </g>

    <g class="contact-row email">
      <circle class="icon-line" cx="34" cy="263" r="16.5"/>
      <rect class="icon-line" x="24" y="256" width="20" height="14"/>
      <path class="icon-line" d="M24 256 l10 8 l10 -8"/>
      <text class="contact" x="61" y="269">lew@slatewellconsulting.co.uk</text>
    </g>

    <g class="accent-band">
      <polygon class="ink" points="0,301 400,301 390,334 0,334"/>
      <polygon class="ink" points="465,301 550,301 550,334 453,334"/>
    </g>
  </g>

  <!-- Brand side -->
  <g class="card card-brand" transform="translate(197 571)">
    <rect class="card-face" width="550" height="355"/>

    <g class="pillars">
      <rect class="ink" x="0" y="43" width="214" height="28"/>
      <text class="pillar" x="13" y="63">Responsible Lending</text>
      <rect class="ink" x="0" y="80" width="133" height="28"/>
      <text class="pillar" x="13" y="100">Fair Charges</text>
      <rect class="ink" x="0" y="122" width="189" height="28"/>
      <text class="pillar" x="13" y="142">Ethical Collections</text>
    </g>

    <g class="brand-lockup">
      <circle class="ink" cx="288" cy="97" r="22"/>
      <text class="brand-name brand-primary" x="316" y="105" textLength="214" lengthAdjust="spacingAndGlyphs">SLATEWELL</text>
      <text class="brand-name brand-secondary" x="341" y="129" textLength="147" lengthAdjust="spacingAndGlyphs">CONSULTING</text>
    </g>

    <g class="accent-band">
      <polygon class="ink" points="0,300 401,300 391,332 0,332"/>
      <polygon class="ink" points="465,300 550,300 550,332 453,332"/>
      <text class="band-text" x="13" y="321">lew@slatewellconsulting.co.uk</text>
    </g>
  </g>

</svg>
</body>
</html>
```